Trade Show Booth Sign Design for Retracting Banner

I need a trade show booth sign designed. It will be for a retractable banner that is double sided with 34 by 81 inch.

I want to incorporate my logo (see attached, have it in other file formats as well) and graphics from my website (https://www.pellacorvaadvisory.com/) with parts or all of the following text.

· Educational Content Creation
o Supplemental Textbook Content Development
o E-learning Content Development
· Curriculum Development
o VKTR/Joint Pillar
o Three Dimensional Learning
· Assessment
o Formative Assessments
o Elementary School, Middle School, High School, College, and Business
· Professional Development
o Training
o Facilitation

Target Market(s)

Education

Industry/Entity Type

Education

Font styles to use
Sans Serif

Colors

Designer to choose colors to be used in the design.

Requirements
Must have
• Eye catching and easy to read design
Nice to have
• Would like to see incorporation of my logo and some of the elements of my website images
Should not have
• N/A

```html
<!DOCTYPE html>
<html lang="en">
<head>
<meta charset="utf-8">
<title>Pella Corva Advisory – Retractable Banner</title>
<link href="https://fonts.googleapis.com/css2?family=Teko:wght@500;600&display=swap" rel="stylesheet">
<style>
  :root {
    --page-bg: #ffffff;
    --chalk: #1d1e20;
    --chalk-edge: #2a2b2e;
    --navy: #142a66;
    --navy-deep: #1b2a5e;
    --sky: #3b86c8;
    --white: #ffffff;
    --rule: #1b2a5e;
    --red: #e3262c;
    --ice: #93cdf0;
    --yellow: #f4d20b;
    --gold: #f1b526;
    --text: #ffffff;
  }
  * { box-sizing: border-box; margin: 0; padding: 0; }
  html, body {
    width: 1200px; height: 1066px; overflow: hidden;
    background: var(--page-bg);
  }
  .banner {
    position: absolute; left: 390px; top: 33px;
    width: 420px; height: 1000px;
    display: flex; flex-direction: column;
    box-shadow: 0 4px 14px rgba(0,0,0,.25);
    font-family: "Teko", "Arial Narrow", sans-serif;
  }
  .masthead {
    height: 402px;
    background: radial-gradient(ellipse at 50% 40%, var(--chalk-edge), var(--chalk) 70%);
    position: relative;
  }
  .masthead__art {
    position: absolute; left: 16px; right: 16px; top: 0; height: 130px;
    background: linear-gradient(90deg, #c9302c 0%, #3d6fd0 22%, #f0cf1c 48%, #ee7d1f 72%, #4eb2e4 100%);
    opacity: .55; border-radius: 0 0 10px 10px;
  }
  .brand {
    position: absolute; left: 0; right: 0; top: 190px;
    text-align: center; color: var(--white);
    font-weight: 600; font-size: 80px; line-height: .85;
    text-transform: uppercase; letter-spacing: 1px;
  }
  .services { display: flex; flex-direction: column; }
  .service {
    height: 128px; display: flex;
  }
  .service__icon-cell {
    width: 143px; background: var(--white);
    border-bottom: 4px solid var(--rule);
    display: flex; align-items: center; justify-content: center;
  }
  .service:last-child .service__icon-cell { border-bottom: none; }
  .service__icon {
    width: 92px; height: 92px; border-radius: 50%;
    background: radial-gradient(circle, #24357a, var(--navy-deep));
    border: 3px solid #d9dce3;
  }
  .service__body {
    flex: 1; background: var(--navy);
    padding: 12px 0 0 28px; color: var(--text);
  }
  .service__title {
    font-weight: 600; font-size: 34px; line-height: .9;
    text-transform: uppercase; letter-spacing: .3px;
    margin-bottom: 6px;
  }
  .service__title--red { color: var(--red); }
  .service__title--ice { color: var(--ice); }
  .service__title--yellow { color: var(--yellow); }
  .service__title--gold { color: var(--gold); }
  .service__list { list-style: none; }
  .service__list li {
    font-weight: 500; font-size: 13px; line-height: 1.2;
    text-transform: uppercase; padding-left: 11px; position: relative;
  }
  .service__list li::before {
    content: ""; position: absolute; left: 0; top: 4px;
    width: 5px; height: 5px; border-radius: 50%; background: var(--white);
  }
  .footer { height: 86px; display: flex; }
  .footer__block { width: 143px; background: var(--navy-deep); }
  .footer__url {
    flex: 1; background: var(--sky); color: var(--white);
    display: flex; align-items: center; justify-content: center;
    font-weight: 600; font-size: 18px; letter-spacing: .3px;
    text-transform: uppercase;
  }
</style>
</head>
<body>
  <main class="banner">
    <header class="masthead">
      <div class="masthead__art" role="img" aria-label="Crumpled paper light bulbs in red, blue, yellow, orange and light blue hanging from cords, the centre bulb glowing"></div>
      <h1 class="brand">Pella Corva<br>Advisory</h1>
    </header>

    <section class="services">
      <article class="service">
        <div class="service__icon-cell"><div class="service__icon" role="img" aria-label="Icon: head in profile with a lightbulb and ideas"></div></div>
        <div class="service__body">
          <h2 class="service__title service__title--red">Educational<br>Content Creation</h2>
          <ul class="service__list">
            <li>Supplemental Textbook Content Development</li>
            <li>E-Learning Content Development</li>
          </ul>
        </div>
      </article>

      <article class="service">
        <div class="service__icon-cell"><div class="service__icon" role="img" aria-label="Icon: presenter at a whiteboard with charts in front of an audience"></div></div>
        <div class="service__body">
          <h2 class="service__title service__title--ice">Curriculum<br>Development</h2>
          <ul class="service__list">
            <li>VKTR/Joint Pillar</li>
            <li>Three Dimensional Learning</li>
          </ul>
        </div>
      </article>

      <article class="service">
        <div class="service__icon-cell"><div class="service__icon" role="img" aria-label="Icon: science flask surrounded by lab and study symbols"></div></div>
        <div class="service__body">
          <h2 class="service__title service__title--yellow">Assessment</h2>
          <ul class="service__list">
            <li>Formative Assessments</li>
            <li>Elementary School, Middle School,<br>High School, College, and Business</li>
          </ul>
        </div>
      </article>

      <article class="service">
        <div class="service__icon-cell"><div class="service__icon" role="img" aria-label="Icon: hand holding a lightbulb with growth charts"></div></div>
        <div class="service__body">
          <h2 class="service__title service__title--gold">Professional<br>Development</h2>
          <ul class="service__list">
            <li>Training</li>
            <li>Facilitation</li>
          </ul>
        </div>
      </article>
    </section>

    <footer class="footer">
      <div class="footer__block"></div>
      <div class="footer__url">www.pellacorvaadvisory.com</div>
    </footer>
  </main>
</body>
</html>
```